Label design for an exciting new Vodka brand

We need a label design for a dynamic new Vodka brand called 'Pale lantern Vodka'. It is a crisp and versatile liquid with a clean and smooth finish. It should appeal to 21-39 year olds, with a slight female skew. Colours, fonts and styles should be modern and relatively neutral - take inspiration from the brand pictures attached.

Target Market(s)

21-39 year olds, both male and female, but with a slight female skew

```html
<!DOCTYPE html>
<html lang="en">
<head>
<meta charset="utf-8">
<title>Pale lantern Vodka – Label</title>
<link href="https://fonts.googleapis.com/css2?family=Anton&display=swap" rel="stylesheet">
<style>
  :root {
    --label-bg: #f6ebe7;
    --salmon: #e49a83;
    --ink: #111111;
    --gold-light: #fdf7d6;
    --gold-mid: #e9d396;
    --gold-deep: #c29a3e;
    --seal: #e2c37a;
  }
  html, body {
    margin: 0;
    padding: 0;
    width: 894px;
    height: 1200px;
    overflow: hidden;
    background: var(--label-bg);
  }
  .label {
    position: relative;
    width: 894px;
    height: 1200px;
    background: var(--label-bg);
    font-family: "Anton", "Impact", sans-serif;
    color: var(--salmon);
    text-transform: uppercase;
  }
  .seal {
    position: absolute;
    left: 640px;
    top: 60px;
    width: 200px;
    height: 200px;
    border-radius: 50%;
    background: var(--seal);
  }
  .brand-name {
    position: absolute;
    left: 0;
    top: 70px;
    width: 894px;
    margin: 0;
    font-weight: 400;
    font-size: 240px;
    line-height: 1.04;
    letter-spacing: 0;
    color: var(--salmon);
  }
  .brand-name .line {
    display: block;
    white-space: nowrap;
  }
  .line-pale { padding-left: 150px; }
  .line-lantern { padding-left: 48px; }
  .line-vodka { padding-left: 220px; }
  .tagline {
    position: absolute;
    left: 0;
    top: 962px;
    width: 894px;
    margin: 0;
    text-align: center;
    font-size: 56px;
    line-height: 1;
    letter-spacing: -1px;
    transform: scaleX(0.9);
  }
  .tagline .gold {
    background: linear-gradient(90deg, var(--gold-mid) 0%, var(--gold-deep) 55%, var(--gold-light) 100%);
    -webkit-background-clip: text;
    background-clip: text;
    color: transparent;
  }
  .volume {
    position: absolute;
    left: 0;
    top: 1116px;
    width: 894px;
    margin: 0;
    text-align: center;
    font-size: 28px;
    color: var(--ink);
  }
</style>
</head>
<body>
  <main class="label">
    <div class="seal" aria-hidden="true"></div>

    <h1 class="brand-name">
      <span class="line line-pale">Pale</span>
      <span class="line line-lantern">Lantern</span>
      <span class="line line-vodka">Vodka</span>
    </h1>

    <p class="tagline">Crisp and versatile with a<br>clean and <span class="gold">smoooth</span> finish</p>

    <p class="volume">700ml</p>
  </main>
</body>
</html>
```